Australian Consultant Pharmacist Business Needs A3 Flyer for Medical Centre

Our business has just secured a deal in a medical centre to offer our consulting services. We have installed our software on the doctors computers and would like to have an A3 flyer to put on their walls to remind them about our services and explain very briefly how to use our simple software.

We would like the flyer to be vibrant and very simple whilst conveying our message of improving patient health outcomes and illustrating how to use our software and service.

We provide Home Medicine Reviews (HMR) for General Practitioners (GP) at medical centres.

There are 3 pathways for a GP to use our service, all resulting in the same outcome.

The outcome is the Dr sends us a referral for a HMR for their patient. In turn they receive a report back after we have performed the HMR.

Pathways
1.
-GP Opens Patient File in medical prescribing software
-If patient is eligible for a HMR, an alert will pop up in bottom right hand corner (approx 30 seconds)
- Click Send Referral
- New page opens, select reason for referral ie. several medicines
- Press Send - referral is sent electronically to Pharmacist

2.
No alert pops up but GP still wants to refer.
Right click Chime Notify program - Chime Notify program is identified by the bell shape icon in the bottom right side of the desktop tray next to the time.
Click refer current patient - this will refer the patient currently open on the GP prescribing software

3. GP would like to send HMR Referal via Fax.
Fax number 03 7192 3048

I have attached some examples of how the software and service works, including screen shots and some power points. I would like to use these as ideas for our A3 Flyer.

Good Luck!

Target Market(s)

Doctors

Industry/Entity Type

Health Service

Colors
f37122
0455a3
3176b5
33a6d7
f68d4c

Requirements
Must have
• Our company name - Brightwell Care HMR
• Our email brightwellcarehmr@fernmail.example
• our fax number
• the 3 ways to use our service and how
• prefer images and short keyword descriptions
• convey idea of improving patient health
• ensure our service comes accross as simple and effecient
Nice to have
• images, vibrant,
Should not have
• lengthy descriptions

```html
<!DOCTYPE html>
<html lang="en">
<head>
<meta charset="utf-8">
<title>Brightwell Care HMR – Flyer</title>
<link rel="stylesheet" href="https://fonts.googleapis.com/css2?family=Crimson+Text:wght@400;700&family=Arimo:ital,wght@0,400;0,700;1,400&display=swap">
<style>
:root{
  --blue-deep:#0455a3;
  --blue-mid:#1a75c0;
  --blue-soft:#3176b5;
  --blue-sky:#33a6d7;
  --orange:#f37122;
  --orange-soft:#f68d4c;
  --band-grey:#7b7b7b;
  --text-grey:#474747;
  --page-bg:#e9eaec;
  --white:#ffffff;
}
*{box-sizing:border-box;margin:0;padding:0}
html,body{width:1200px;height:960px;overflow:hidden;background:var(--page-bg)}
.flyer{position:absolute;left:5px;top:59px;width:1190px;height:842px;background:var(--white);overflow:hidden;font-family:"Arimo",Arial,sans-serif}
.brand{position:absolute;left:0;width:1202px;top:28px;text-align:center;color:var(--blue-mid);font-family:"Crimson Text",Georgia,serif;font-weight:400;font-size:58px;line-height:1}
.tagline{position:absolute;left:0;width:1202px;top:92px;text-align:center;color:var(--blue-mid);font-family:"Crimson Text",Georgia,serif;font-size:30px;line-height:1}
.hero-photo{position:absolute;left:944px;top:0;width:246px;height:156px;background:linear-gradient(100deg,#f4f1ec 0%,#d8cbb8 35%,#9fb3c9 70%,#7c95b5 100%)}
.band{position:absolute;left:0;top:156px;width:1190px;height:62px;background:var(--band-grey);color:var(--white);font-style:italic;font-size:20px;display:flex;align-items:center;justify-content:center}
.headline{position:absolute;left:0;width:1190px;top:238px;text-align:center;color:var(--blue-mid);font-family:"Crimson Text",Georgia,serif;font-weight:700;font-size:27px}
.intro{position:absolute;left:54px;width:1082px;top:287px;text-align:center;color:var(--text-grey);font-size:14.5px;line-height:21px}
.panel{position:absolute;background:linear-gradient(160deg,var(--blue-mid) 0%,var(--blue-soft) 45%,var(--blue-deep) 100%);border-radius:0 10px 4px 4px}
.panel-1{left:87px;top:360px;width:278px;height:404px}
.panel-2{left:465px;top:429px;width:278px;height:333px;background:linear-gradient(160deg,#2a86cc 0%,#4a8fc8 50%,#2f72b3 100%)}
.panel-3{left:847px;top:574px;width:277px;height:184px}
.tab{position:absolute;height:37px;width:154px;background:var(--white);border:2px solid var(--blue-mid);border-radius:9px;color:var(--blue-deep);font-family:"Crimson Text",Georgia,serif;font-weight:700;font-size:19px;letter-spacing:.5px;display:flex;align-items:center;justify-content:center}
.tab-1{left:224px;top:370px}
.tab-2{left:604px;top:441px}
.tab-3{left:982px;top:589px}
.steps{position:absolute;list-style:none;color:var(--white);font-weight:700;font-size:12.5px;line-height:15.2px}
.steps li{position:relative;padding-left:14px;margin-bottom:15px}
.steps li::before{content:"";position:absolute;left:0;top:5px;width:6px;height:6px;border-radius:50%;background:var(--white)}
.steps-1{left:165px;top:427px;width:162px}
.steps-2{left:559px;top:488px;width:160px}
.steps-3{left:932px;top:642px;width:152px}
.shot{position:absolute;border-radius:50%;border:2px solid var(--blue-mid);overflow:hidden}
.shot-a{left:33px;top:407px;width:112px;height:110px;background:linear-gradient(180deg,#ffffff 0%,#f4f4f4 70%,#c9d3df 100%)}
.shot-b{left:33px;top:527px;width:112px;height:110px;background:linear-gradient(180deg,#f2f2f2 0%,#d9d9d9 100%)}
.shot-c{left:33px;top:647px;width:112px;height:110px;background:linear-gradient(90deg,#e9a27a 0%,#f2f2f2 25%,#dedede 100%)}
.shot-d{left:393px;top:474px;width:158px;height:156px;background:linear-gradient(180deg,#ffffff 0%,#fbf5f1 70%,#cfd8e3 100%)}
.shot-e{left:775px;top:600px;width:136px;height:136px;background:linear-gradient(135deg,#c9b79d 0%,#6b625a 55%,#2b2b2b 100%)}
.pills-photo{position:absolute;left:781px;top:350px;width:365px;height:200px;background:radial-gradient(ellipse at 55% 70%,#e9b8a0 0%,#9ec6e4 35%,#eef3f6 65%,#ffffff 85%)}
.contact{position:absolute;left:0;width:1162px;top:794px;text-align:center;color:var(--blue-mid);font-family:"Crimson Text",Georgia,serif;font-size:24px}
</style>
</head>
<body>
<main class="flyer">
  <header>
    <h1 class="brand">Brightwell Care HMR</h1>
    <p class="tagline">Improving Patient Outcomes</p>
    <div class="hero-photo" role="img" aria-label="Photo of a pharmacist talking with an older couple in a pharmacy"></div>
  </header>

  <p class="band">Providing Home Medicine Reviews (HMR) for General Practitioners&nbsp; (GP) at medical centres.</p>

  <h2 class="headline">There are 3 pathways for a GP to use our service, all resulting in the same outcome.</h2>
  <p class="intro">The result is the Dr sends us a referral for a HMR for their patient. Referral is sent via an encrypted secure electronic transmission. HMR Pharmacist receives referral and conducts interview.GP Receives Medication Management Plan – Review and Claim MBS 900.</p>

  <section class="panel panel-1"></section>
  <div class="tab tab-1">PATHWAY 1</div>
  <ul class="steps steps-1">
    <li>GP Opens Patient File in medical prescribing software</li>
    <li>If patient is eligible for a HMR, an alert will pop up in bottom right hand corner (approx 30 seconds)</li>
    <li>Click Send Referral</li>
    <li>New page opens, select reason for referral ie. several medicines</li>
    <li>Press Send - referral is sent electronically to Pharmacist</li>
  </ul>
  <div class="shot shot-a" role="img" aria-label="Screenshot of the desktop tray showing the alert program icon"></div>
  <div class="shot shot-b" role="img" aria-label="Screenshot of the referral alert window with Send Referral button"></div>
  <div class="shot shot-c" role="img" aria-label="Screenshot of the referral form with reasons for referral"></div>

  <section class="panel panel-2"></section>
  <div class="tab tab-2">PATHWAY 2</div>
  <ul class="steps steps-2">
    <li>No alert pops up but GP still wants to refer.</li>
    <li>Right click Chime Notify program - Chime Notify program is identified by the bell shape icon in the bottom right side of the desktop tray next to the time.</li>
    <li>Click refer current patient - this will refer the patient currently open on the GP prescribing software</li>
  </ul>
  <div class="shot shot-d" role="img" aria-label="Annotated screenshot of the desktop tray icon with right-click steps"></div>

  <div class="pills-photo" role="img" aria-label="Photo of a glass of water beside a pile of colourful tablets and capsules"></div>

  <section class="panel panel-3"></section>
  <div class="tab tab-3">PATHWAY 3</div>
  <ul class="steps steps-3">
    <li>GP would like to send HMR Referal via Fax.</li>
    <li>Fax number<br>03 7192 3048</li>
  </ul>
  <div class="shot shot-e" role="img" aria-label="Photo of a document being fed into a fax machine"></div>

  <p class="contact">For any assistance send us a mail at brightwellcarehmr@fernmail.example</p>
</main>
</body>
</html>
```